Webdesign für Juwelier-Geschäft
Zielgruppe
Wir sind ein Juwelier Laden. Unsere Zielgruppe sind Frauen und Männer jeden Alters, die an Gold- und Silberschmuck/Uhren/Diamanten/Trauringen interessiert sind.
Aufgabenstellung
Edles Design in Gold, Schwarz/Grau, Weiß.
Bildelemente für die Artikelkategorien Ketten, Ohrringe und Ringe etc.
Ein Logo besteht bereits.

```html
<!DOCTYPE html>
<html lang="de">
<head>
<meta charset="utf-8">
<title>Juwelier Corvin – Startseite</title>
<link href="https://fonts.googleapis.com/css2?family=Cinzel:wght@400&family=Lato:wght@400;700&display=swap" rel="stylesheet">
<style>
  :root {
    --gold: #d9ae4f;
    --gold-soft: #c9a055;
    --hero-dark: #262324;
    --hero-mid: #35302e;
    --tile-bg: #2b2828;
    --tile-border: #4d4846;
    --footer-bg: #252327;
    --footer-text: #8c8785;
    --white: #ffffff;
    --nav-text: #f2efe9;
  }
  * { margin: 0; padding: 0; box-sizing: border-box; }
  html, body { width: 1200px; height: 634px; overflow: hidden; background: var(--hero-dark); }
  body { font-family: "Lato", Arial, sans-serif; position: relative; }

  .hero {
    position: absolute; left: 0; top: 0; width: 1200px; height: 570px;
    background: radial-gradient(ellipse at 35% 30%, var(--hero-mid) 0%, var(--hero-dark) 70%);
    overflow: hidden;
  }
  .hero-ornament {
    position: absolute; left: -120px; top: 85px; width: 280px; height: 340px;
    border-radius: 50%;
    background: radial-gradient(circle at 50% 50%, rgba(160,120,70,0.38) 0%, rgba(120,90,55,0.22) 45%, rgba(60,50,40,0) 72%);
  }
  .hero-photo {
    position: absolute; left: 560px; top: 0; width: 640px; height: 570px;
    background:
      radial-gradient(ellipse at 58% 30%, #c99a7c 0%, #a7765c 28%, rgba(90,70,60,0.6) 55%, rgba(45,40,40,0) 78%),
      radial-gradient(ellipse at 70% 85%, #b98463 0%, rgba(120,85,65,0.5) 40%, rgba(45,40,40,0) 70%),
      linear-gradient(90deg, rgba(38,35,36,1) 0%, rgba(60,55,55,0.3) 40%, #4a4443 100%);
  }

  .logo { position: absolute; left: 150px; top: 20px; width: 150px; }
  .logo-name {
    font-family: "Cinzel", Georgia, serif; color: var(--gold);
    font-size: 22px; line-height: 24px; letter-spacing: 1px;
  }
  .logo-tagline {
    font-size: 8.5px; color: var(--gold); letter-spacing: 0.3px; margin-top: 4px;
  }

  .main-nav { position: absolute; left: 461px; top: 0; display: flex; }
  .main-nav a {
    display: block; font-size: 12px; font-weight: 700; color: var(--nav-text);
    text-decoration: none; padding: 27px 8px 0; height: 58px; margin-right: 7px;
  }
  .main-nav a.is-active { color: var(--gold); border-bottom: 2px solid var(--gold); }

  .cart { position: absolute; left: 1017px; top: 26px; display: flex; align-items: center; gap: 3px; color: var(--white); font-size: 11px; }

  .headline {
    position: absolute; left: 152px; top: 157px;
    font-family: "Cinzel", Georgia, serif; font-weight: 400;
    font-size: 43px; line-height: 45px; letter-spacing: 1px;
    color: var(--white);
  }
  .headline .accent { color: var(--gold); display: block; }

  .categories { position: absolute; left: 150px; top: 421px; width: 900px; height: 108px; }
  .category {
    position: absolute; top: 0; width: 92px; height: 108px;
    background: var(--tile-bg); border: 1px solid var(--tile-border);
  }
  .category-image {
    position: absolute; left: 12px; top: 6px; width: 68px; height: 64px;
    background: radial-gradient(circle, #e6bb55 0%, #b8862f 45%, rgba(43,40,40,0) 72%);
  }
  .category-label {
    position: absolute; left: 0; right: 0; top: 80px; text-align: center;
    color: var(--white); font-size: 11.5px; font-weight: 700; letter-spacing: 0.4px; text-transform: uppercase;
  }

  .site-footer {
    position: absolute; left: 0; top: 570px; width: 1200px; height: 64px; background: var(--footer-bg);
  }
  .copyright { position: absolute; left: 152px; top: 24px; font-size: 11.5px; color: var(--footer-text); }
  .social { position: absolute; left: 894px; top: 24px; display: flex; gap: 21px; }
  .social-link { width: 14px; height: 14px; border-radius: 50%; background: #6e6a69; display: block; }
</style>
</head>
<body>
  <section class="hero">
    <div class="hero-ornament" role="img" aria-label="Goldenes Mandala-Ornament als Hintergrunddekor"></div>
    <div class="hero-photo" role="img" aria-label="Porträt einer Frau mit goldenem Halsschmuck, Ohrringen und Armband"></div>

    <div class="logo">
      <div class="logo-name">JUWELIER CORVIN</div>
      <div class="logo-tagline">TRAURINGE | UHREN | SCHMUCK</div>
    </div>

    <nav class="main-nav">
      <a href="#" class="is-active">Startseite</a>
      <a href="#">Über uns</a>
      <a href="#">Geschäft</a>
      <a href="#">Kontakt</a>
    </nav>

    <div class="cart">
      <svg width="16" height="13" viewBox="0 0 16 13" fill="none" stroke="#fff" stroke-width="1.2">
        <path d="M0.5 1h2.5l2 8h8l1.5-6H4"/>
        <circle cx="6" cy="11.5" r="1"/><circle cx="12" cy="11.5" r="1"/>
      </svg>
      <span>(0)</span>
    </div>

    <h1 class="headline">
      DUIS AUTE
      <span class="accent">IRURE DOLOR IN</span>
      <span class="accent">REPREHENDERIT</span>
    </h1>

    <div class="categories">
      <div class="category" style="left:0"><div class="category-image" role="img" aria-label="Goldketten"></div><div class="category-label">Ketten</div></div>
      <div class="category" style="left:161px"><div class="category-image" role="img" aria-label="Goldringe"></div><div class="category-label">Ringe</div></div>
      <div class="category" style="left:323px"><div class="category-image" role="img" aria-label="Trauringe mit Diamant"></div><div class="category-label">Trauringe</div></div>
      <div class="category" style="left:484px"><div class="category-image" role="img" aria-label="Goldene Taschenuhr"></div><div class="category-label">Uhren</div></div>
      <div class="category" style="left:646px"><div class="category-image" role="img" aria-label="Goldohrringe mit Perlen"></div><div class="category-label">Ohrringe</div></div>
      <div class="category" style="left:808px"><div class="category-image" role="img" aria-label="Goldenes Armband"></div><div class="category-label">Armbänder</div></div>
    </div>
  </section>

  <footer class="site-footer">
    <p class="copyright">Copyright 2022. Alle Rechte vorbehalten.</p>
    <div class="social">
      <a href="#" class="social-link" aria-label="Soziales Netzwerk 1"></a>
      <a href="#" class="social-link" aria-label="Soziales Netzwerk 2"></a>
      <a href="#" class="social-link" aria-label="Videoplattform"></a>
      <a href="#" class="social-link" aria-label="Kurznachrichtendienst"></a>
      <a href="#" class="social-link" aria-label="Berufsnetzwerk"></a>
    </div>
  </footer>
</body>
</html>
```